Brivanta.com the Free Online Tutorial Needs a New Web Design

We need a new web design for our existing website, Brivanta.com. We provide a Free Online Tutorial of any code, like HTML, CSS, PHP, jDom, javascript etc, including online editor.
We would like to see designs that interesting, simple, interactive, and be a very comfortable place to read in a long time.
We need 2 pages design for:
1. Home Page (http://brivanta.com) and
2. Listing Page (http://brivanta.com/tutorial/833/sql/sql-basics/sql-and-or-operator.html)
For Listing Page We need nice "Left Menu" at left side and Content Page (min 728px) at right side.
I need File PSD and/or Vector Only, without HTML code.
Online
2 page

```html
<!DOCTYPE html>
<html lang="en">
<head>
<meta charset="utf-8">
<title>Brivanta – Free Online Tutorials</title>
<link href="https://fonts.googleapis.com/css2?family=Fira+Sans:ital,wght@0,400;0,500;0,700;1,700&family=Roboto+Condensed:ital,wght@0,400;0,700;1,700&display=swap" rel="stylesheet">
<style>
:root{
  --page:#e8e8ea;
  --header:#2f2f31;
  --footer:#3a3a3c;
  --footer-bar:#2c2c2e;
  --ink:#1f1f1f;
  --panel:#ffffff;
  --card:#f7f7f9;
  --blue:#1e88d6;
  --green:#5cb030;
  --red:#e8413a;
  --yellow:#f6b81a;
  --html:#e44d26;
  --css:#1f6fc5;
  --js:#5fa51c;
  --php:#7a86b8;
  --sql:#b8285a;
  --jdom:#2aa5d8;
  --nova:#e8911a;
  --json:#333333;
  --canvas:#8bc53f;
  --editor:#6d87c8;
  --ribbon:#7a7a7c;
}
*{box-sizing:border-box;margin:0;padding:0}
html,body{width:904px;height:1200px;overflow:hidden}
body{background:var(--page);font-family:"Fira Sans",sans-serif;color:var(--ink);position:relative}
a{color:inherit;text-decoration:none}
.stripe{background:linear-gradient(to right,var(--blue) 0 25%,var(--green) 25% 50%,var(--red) 50% 75%,var(--yellow) 75%)}

/* header */
.site-header{position:absolute;left:0;top:0;width:904px;height:36px;background:var(--header);border-bottom:1px solid #111}
.brand{position:absolute;left:84px;top:5px;display:flex;align-items:center;gap:6px;font-family:"Roboto Condensed",sans-serif;font-size:24px;color:#fff;line-height:26px}
.brand-mark{width:22px;height:22px}
.tagline{position:absolute;left:224px;top:10px;font-family:"Roboto Condensed",sans-serif;font-size:13px;color:#d9d9d9}
.search{position:absolute;left:545px;top:9px;width:132px;height:19px;background:#f1f1f1;border-radius:2px;font-size:10px;color:#9a9a9a;padding:3px 5px}
.search svg{position:absolute;right:5px;top:4px}
.sign-in{position:absolute;left:705px;top:10px;font-family:"Roboto Condensed",sans-serif;font-size:13px;color:#fff}
.sign-up{position:absolute;left:750px;top:6px;width:60px;height:24px;background:#4a4a4d;border-radius:2px;font-family:"Roboto Condensed",sans-serif;font-size:13px;color:#fff;padding:4px 0 0 13px}
.sign-up::before{content:"";position:absolute;left:0;top:0;width:4px;height:24px;background:linear-gradient(var(--blue) 0 25%,var(--green) 25% 50%,var(--red) 50% 75%,var(--yellow) 75%)}

/* sidebar */
.sidebar{position:absolute;left:67px;top:58px;width:229px;height:486px;background:var(--panel)}
.sidebar-title{font-family:"Roboto Condensed",sans-serif;font-style:italic;font-weight:700;font-size:17px;color:#333;padding:8px 0 0 18px;height:33px;border-bottom:1px solid #e6e6e6}
.nav{list-style:none;font-size:10.5px;line-height:13px;position:absolute;left:0;top:0;width:100%}
.nav li{position:absolute;white-space:nowrap}
.nav-home{left:17px;top:40px;width:163px;height:30px;border:1px solid #bbb;border-right:none;padding:8px 0 0 12px;font-weight:500}
.nav-home::before{content:"";position:absolute;left:-1px;top:-1px;width:3px;height:30px;background:linear-gradient(var(--blue) 0 25%,var(--green) 25% 50%,var(--red) 50% 75%,var(--yellow) 75%)}
.nav-home svg.arrow{position:absolute;right:-13px;top:-1px}
.nav-home svg.house{vertical-align:-1px;margin-right:4px}
.divider{position:absolute;left:0;top:444px;width:229px;height:1px;background:#e2e2e2}
.tryit-link{position:absolute;left:29px;top:454px;font-family:"Roboto Condensed",sans-serif;font-size:13px;display:flex;align-items:center;gap:5px}
.tryit-link .code-badge{width:22px;height:22px;border-radius:50%;background:#ececee;font-size:10px;text-align:center;line-height:22px;font-family:"Fira Sans",sans-serif}
.ads{position:absolute;left:67px;top:567px;width:229px;height:363px;background:var(--panel);display:flex;align-items:center;justify-content:center;font-size:20px;font-weight:500}

/* main */
.hero{position:absolute;left:308px;top:58px;width:512px;height:263px;overflow:hidden}
.hero-photo{position:absolute;inset:0;background:radial-gradient(ellipse at 70% 80%,#b8b8b8 0%,#8a8a8a 35%,#5e5e5e 75%,#4a4a4a 100%)}
.hero-copy{position:absolute;left:0;top:52px;width:512px;text-align:center;color:#fff}
.hero-title{font-family:"Roboto Condensed",sans-serif;font-style:italic;font-weight:700;font-size:22px}
.hero-text{margin:12px auto 0;width:440px;font-style:italic;font-weight:700;font-size:10px;line-height:13.5px}
.hero-button{position:absolute;left:198px;top:186px;width:116px;height:40px;border:1px solid #fff;border-radius:2px;color:#fff;font-style:italic;font-weight:700;font-size:10.5px;text-align:center;line-height:38px}
.hero .stripe{position:absolute;left:0;bottom:0;width:100%;height:4px}

.section-title{position:absolute;left:308px;font-weight:500;font-size:17px;color:#444}
.grid{position:absolute;left:308px;display:grid;grid-template-columns:repeat(4,123px);column-gap:7px;row-gap:13px}
.card{position:relative;width:123px;height:163px;background:var(--card);border:1px solid #bdbdc0;overflow:hidden}
.card-face{height:128px;display:flex;flex-direction:column;align-items:center;padding-top:20px}
.card-name{font-family:"Roboto Condensed",sans-serif;font-weight:700;font-size:17px;letter-spacing:.5px}
.card-square{width:62px;height:62px;margin-top:8px}
.card .stripe{height:3px}
.card-label{text-align:center;font-weight:500;font-size:11.5px;padding-top:9px}
.try .card-face{padding-top:42px}
.try .card-name{font-size:10.5px;color:#222}
.try .card-square{width:40px;height:40px;margin-top:6px}
.ribbon{position:absolute;left:0;top:0}

/* footer */
.site-footer{position:absolute;left:0;top:952px;width:904px;height:214px;background:var(--footer);color:#e6e6e6}
.foot-col{position:absolute;top:25px}
.foot-col h3{font-family:"Roboto Condensed",sans-serif;font-weight:700;font-size:12.5px;color:#fff;padding-left:12px;position:relative;margin-left:-12px;margin-bottom:6px}
.foot-col h3::before{content:"";position:absolute;left:0;top:0;width:2px;height:15px;background:linear-gradient(var(--blue) 0 25%,var(--green) 25% 50%,var(--red) 50% 75%,var(--yellow) 75%)}
.foot-col ul{list-style:none;font-family:"Roboto Condensed",sans-serif;font-size:10.5px;line-height:16.2px}
.social{display:flex;gap:4px;margin-top:6px}
.social span{width:21px;height:21px;border-radius:50%;background:#fff;display:block}
.footer-bar{position:absolute;left:0;top:1166px;width:904px;height:34px;background:var(--footer-bar);border-top:1px solid #555;font-size:10.5px;color:#cfcfcf}
.footer-bar .left{position:absolute;left:67px;top:11px}
.footer-bar .right{position:absolute;right:84px;top:11px}
</style>
</head>
<body>

<header class="site-header">
  <a class="brand" href="#">
    <svg class="brand-mark" viewBox="0 0 22 22"><rect width="22" height="22" fill="#f6b81a"/></svg>
    <span>Brivanta</span>
  </a>
  <p class="tagline">A Place for Learning and Trying of any Code</p>
  <div class="search">Search
    <svg width="11" height="11" viewBox="0 0 11 11"><circle cx="4.5" cy="4.5" r="3.3" fill="none" stroke="#333" stroke-width="1.5"/><line x1="7" y1="7" x2="10.3" y2="10.3" stroke="#333" stroke-width="1.8"/></svg>
  </div>
  <a class="sign-in" href="#">Sign In</a>
  <a class="sign-up" href="#">Sign up</a>
</header>

<aside class="sidebar">
  <h2 class="sidebar-title">Browse By Category</h2>
  <ul class="nav">
    <li class="nav-home">
      <svg class="house" width="8" height="8" viewBox="0 0 8 8"><path d="M4 0 8 4H7V8H5V5.5H3V8H1V4H0Z" fill="#222"/></svg>Home
      <svg class="arrow" width="14" height="30" viewBox="0 0 14 30"><path d="M0 .5H1L13 15 1 29.5H0" fill="#fff" stroke="#bbb"/></svg>
    </li>
    <li style="left:31px;top:78px">
      <svg width="7" height="5" viewBox="0 0 7 5" style="margin-right:3px;vertical-align:1px"><path d="M0 0H7L3.5 5Z" fill="#222"/></svg>HTML</li>
    <li style="left:45px;top:102px">HTML4</li>
    <li style="left:45px;top:116px">HTML5</li>
    <li style="left:64px;top:130px">HTML5 Tutorial</li>
    <li style="left:64px;top:145px">HTML5 Canvas Tutorial</li>
    <li style="left:64px;top:159px">HTML5 Canvas Examples</li>
    <li style="left:64px;top:173px">HTML5 All Examples</li>
    <li style="left:40px;top:207px">CSS</li>
    <li style="left:40px;top:236px">JavaScript</li>
    <li style="left:40px;top:265px">PHP</li>
    <li style="left:40px;top:294px">SQL</li>
    <li style="left:40px;top:323px">jDom</li>
    <li style="left:40px;top:352px">JSON</li>
    <li style="left:40px;top:381px">NovaSQL</li>
    <li style="left:40px;top:410px">Regex</li>
  </ul>
  <div class="divider"></div>
  <a class="tryit-link" href="#"><span class="code-badge">&lt;/&gt;</span>Tryit Yourself &gt;&gt;</a>
</aside>

<div class="ads">ads</div>

<section class="hero">
  <div class="hero-photo" role="img" aria-label="Blurred desk photo with glasses and a computer mouse"></div>
  <div class="hero-copy">
    <h1 class="hero-title">The Free Online Tutorials Place</h1>
    <p class="hero-text">Brivanta is a place for Learning, testing, and examples for web building. The Examples in each chapter might be simplified to improve your basic understanding. With Brivanta You will feel much easier than ever to learn about HTML including online code editor for each chapter, so you can edit, modify and execute the code.</p>
  </div>
  <a class="hero-button" href="#">Try It</a>
  <div class="stripe"></div>
</section>

<h2 class="section-title" style="top:338px">Featured Tutorial</h2>
<div class="grid" style="top:369px">
  <a class="card" href="#"><div class="card-face"><span class="card-name">HTML</span><span class="card-square" style="background:var(--html)"></span></div><div class="stripe"></div><p class="card-label">HTML5 Tutorials</p></a>
  <a class="card" href="#"><div class="card-face"><span class="card-name">CSS</span><span class="card-square" style="background:var(--css)"></span></div><div class="stripe"></div><p class="card-label">CSS3 Tutorials</p></a>
  <a class="card" href="#"><div class="card-face"><span class="card-name">JS</span><span class="card-square" style="background:var(--js)"></span></div><div class="stripe"></div><p class="card-label">Javascript Tutorials</p></a>
  <a class="card" href="#"><div class="card-face"><span class="card-name">PHP</span><span class="card-square" style="background:var(--php)"></span></div><div class="stripe"></div><p class="card-label">PHP Tutorials</p></a>
  <a class="card" href="#"><div class="card-face"><span class="card-name">SQL</span><span class="card-square" style="background:var(--sql)"></span></div><div class="stripe"></div><p class="card-label">SQL Tutorials</p></a>
  <a class="card" href="#"><div class="card-face"><span class="card-name">jDom</span><span class="card-square" style="background:var(--jdom)"></span></div><div class="stripe"></div><p class="card-label">JDOM Tutorials</p></a>
  <a class="card" href="#"><div class="card-face"><span class="card-name">NovaSQL</span><span class="card-square" style="background:var(--nova)"></span></div><div class="stripe"></div><p class="card-label">NOVASQL Tutorials</p></a>
  <a class="card" href="#"><div class="card-face"><span class="card-name">JSON</span><span class="card-square" style="background:var(--json)"></span></div><div class="stripe"></div><p class="card-label">JSON Tutorials</p></a>
</div>

<h2 class="section-title" style="top:736px">Featured Tryit Yourself</h2>
<div class="grid" style="top:767px">
  <a class="card try" href="#">
    <svg class="ribbon" width="74" height="74" viewBox="0 0 74 74"><path d="M0 48 48 0H72L0 72Z" fill="var(--ribbon)"/><text x="30" y="33" transform="rotate(-45 30 30)" text-anchor="middle" font-family="Roboto Condensed, sans-serif" font-weight="700" font-style="italic" font-size="9" fill="#fff">Tryit Yourself</text></svg>
    <div class="card-face"><span class="card-name">Editor</span><span class="card-square" style="background:var(--html)"></span></div><div class="stripe"></div><p class="card-label">HTML5 Examples</p></a>
  <a class="card try" href="#">
    <svg class="ribbon" width="74" height="74" viewBox="0 0 74 74"><path d="M0 48 48 0H72L0 72Z" fill="var(--ribbon)"/><text x="30" y="33" transform="rotate(-45 30 30)" text-anchor="middle" font-family="Roboto Condensed, sans-serif" font-weight="700" font-style="italic" font-size="9" fill="#fff">Tryit Yourself</text></svg>
    <div class="card-face"><span class="card-name">Canvas</span><span class="card-square" style="background:var(--canvas)"></span></div><div class="stripe"></div><p class="card-label">Canvas Examples</p></a>
  <a class="card try" href="#">
    <svg class="ribbon" width="74" height="74" viewBox="0 0 74 74"><path d="M0 48 48 0H72L0 72Z" fill="var(--ribbon)"/><text x="30" y="33" transform="rotate(-45 30 30)" text-anchor="middle" font-family="Roboto Condensed, sans-serif" font-weight="700" font-style="italic" font-size="9" fill="#fff">Tryit Yourself</text></svg>
    <div class="card-face"><span class="card-name">Example</span><span class="card-square" style="background:var(--sql)"></span></div><div class="stripe"></div><p class="card-label">SQL Examples</p></a>
  <a class="card try" href="#">
    <svg class="ribbon" width="74" height="74" viewBox="0 0 74 74"><path d="M0 48 48 0H72L0 72Z" fill="var(--ribbon)"/><text x="30" y="33" transform="rotate(-45 30 30)" text-anchor="middle" font-family="Roboto Condensed, sans-serif" font-weight="700" font-style="italic" font-size="9" fill="#fff">Tryit Yourself</text></svg>
    <div class="card-face"><span class="card-name">Editor</span><span class="card-square" style="background:var(--editor)"></span></div><div class="stripe"></div><p class="card-label">Online Code Editor</p></a>
</div>

<footer class="site-footer">
  <div class="foot-col" style="left:79px">
    <h3>Customer Service</h3>
    <ul><li>About</li><li>Terms</li><li>Privacy</li><li>Disclaimer</li><li>Contact</li><li>FAQ</li></ul>
  </div>
  <div class="foot-col" style="left:220px">
    <h3>Random HTML5</h3>
    <ul><li>dl html5</li><li>footer in html5</li><li>Colgroup tag in html</li><li>frameset</li><li>header in html5</li><li>Web Workers</li><li>tfoot tag in html</li><li>rp in html5</li><li>meta in HTML5</li><li>dd tag is used to describ..</li></ul>
  </div>
  <div class="foot-col" style="left:390px">
    <h3>Random Canvas</h3>
    <ul><li>Canvas Fill Style</li><li>Canvas Semicircles</li><li>Canvas Pattern</li><li>Canvas Rectangles</li><li>Canvas Introduction</li><li>Canvas Text Basics</li><li>Canvas Line Width</li><li>Canvas Line Cap</li><li>Canvas Quadratic Curve</li><li>Canvas Custom Paths</li></ul>
  </div>
  <div class="foot-col" style="left:550px">
    <h3>Customer Service</h3>
    <ul><li>JS DOM Object</li><li>JS String match()</li><li>JS DOM Input Button</li><li>JS DOM Input Hidden</li><li>JS Number Positive_Infini..</li><li>Javascript Operators</li><li>JS Math pow(x,y)</li><li>JS Global String()</li><li>JS String toLowerCase()</li><li>JS RegExp lastIndex</li></ul>
  </div>
  <div class="foot-col" style="left:709px">
    <h3>Join Us On Social</h3>
    <div class="social"><span></span><span></span><span></span><span></span></div>
  </div>
</footer>
<div class="footer-bar">
  <span class="left">Privacy Policy</span>
  <span class="right">Brivanta © 2015, All rights reserved</span>
</div>

</body>
</html>
```